Banners for Website and Social Media

Technology Consulting and Services company requires several banners that integrate our logo that can be used on a basic website that we are designing. The design will also be used on social media platforms. Require a variety of sizes and shapes to be included. Need at least two variations for a website header, more variations will put you at the top of the leaderboard.

Target Market(s)

Non-Profit Mental Health Agencies, small business

Font styles to use
Serif

Requirements
Must have
• Show the idea of connecting with our clients. We require the following approximate sizes, they do not have to be exact:

2 x variations 1080px x 600px for website header
1 x 1128px x 191px for Brindlepost
1 x 590px x 175px for Email Marketing
1 x 300px x 250px for Advertising

Colours should compliment the logo that has been provided.
Nice to have
• Could integrate key words and phrases in the graphic but not standout as a tagline or title.

- Engaged
- Ethical Technology
- Support
- Connected
Should not have
• Banner should avoid having people in it. Prefer a more abstract feel.

```html
<!DOCTYPE html>
<html lang="en">
<head>
<meta charset="utf-8">
<title>Kestrelane Technology – Banner Set</title>
<link rel="stylesheet" href="https://fonts.googleapis.com/css2?family=Montserrat:wght@600;700&display=swap">
<style>
  :root {
    --page-bg: #e9e9ec;
    --banner-blue: #1d5bb0;
    --banner-indigo: #3a2fa6;
    --banner-purple: #5c1c9e;
    --glow: rgba(120, 150, 255, 0.28);
    --wave-light: rgba(150, 175, 255, 0.22);
    --text-light: #ffffff;
    --label-blue: #2d5ba6;
  }
  * { box-sizing: border-box; margin: 0; padding: 0; }
  html, body { width: 900px; height: 1200px; overflow: hidden; }
  body {
    position: relative;
    background: var(--page-bg);
    font-family: "Montserrat", Arial, sans-serif;
    color: var(--text-light);
  }
  .banner {
    position: absolute;
    overflow: hidden;
    background:
      radial-gradient(ellipse 70% 55% at 70% 60%, var(--glow), transparent 70%),
      linear-gradient(120deg, var(--banner-blue) 0%, var(--banner-indigo) 55%, var(--banner-purple) 100%);
  }
  .banner__wave {
    position: absolute;
    inset: 0;
    background:
      radial-gradient(ellipse 60% 22% at 65% 45%, var(--wave-light), transparent 75%),
      radial-gradient(ellipse 50% 18% at 80% 70%, var(--wave-light), transparent 75%);
    transform: rotate(-8deg) scale(1.2);
  }
  .banner__word {
    position: absolute;
    font-weight: 600;
    letter-spacing: 0.12em;
    text-transform: uppercase;
    white-space: nowrap;
    line-height: 1;
  }
  .brand {
    position: absolute;
    display: flex;
    flex-direction: column;
    align-items: center;
    transform: translateX(-50%);
  }
  .brand__dot {
    border: 2px solid var(--text-light);
    border-radius: 50%;
  }
  .brand__name {
    font-weight: 600;
    text-transform: uppercase;
    white-space: nowrap;
    letter-spacing: 0.03em;
    line-height: 1;
  }
  .format-label {
    position: absolute;
    left: 15px;
    font-weight: 700;
    font-size: 14px;
    letter-spacing: 0.08em;
    text-transform: uppercase;
    color: var(--label-blue);
  }

  /* Website header */
  .banner--website { left: 126px; top: 0; width: 648px; height: 360px; }
  .banner--website .banner__word { left: 54px; font-size: 15px; }
  .banner--website .brand { left: 324px; top: 246px; }
  .banner--website .brand__dot { width: 60px; height: 60px; margin-bottom: 12px; }
  .banner--website .brand__name { font-size: 14px; }

  /* Brindlepost header */
  .banner--social { left: 111px; top: 510px; width: 678px; height: 111px; }
  .banner--social .banner__word { font-size: 13px; }
  .banner--social .brand { left: 590px; top: 18px; }
  .banner--social .brand__dot { width: 46px; height: 46px; margin-bottom: 8px; }
  .banner--social .brand__name { font-size: 10px; }

  /* Email marketing */
  .banner--email { left: 270px; top: 762px; width: 357px; height: 105px; }
  .banner--email .banner__word { font-size: 8px; }
  .banner--email .brand { left: 288px; top: 20px; }
  .banner--email .brand__dot { width: 32px; height: 32px; margin-bottom: 6px; }
  .banner--email .brand__name { font-size: 6.5px; }

  /* Advertising */
  .banner--ad { left: 360px; top: 984px; width: 180px; height: 150px; }
  .banner--ad .banner__word { left: 12px; font-size: 7px; }
  .banner--ad .brand { left: 90px; top: 90px; }
  .banner--ad .brand__dot { width: 28px; height: 28px; margin-bottom: 5px; }
  .banner--ad .brand__name { font-size: 7px; }
</style>
</head>
<body>

  <section class="banner banner--website">
    <div class="banner__wave" role="img" aria-label="Flowing blue-to-purple dotted wave mesh"></div>
    <span class="banner__word" style="top:54px">Support</span>
    <span class="banner__word" style="top:90px">Engaged</span>
    <span class="banner__word" style="top:129px">Connected</span>
    <span class="banner__word" style="top:168px">Ethical Technology</span>
    <div class="brand">
      <span class="brand__dot"></span>
      <span class="brand__name">Kestrelane Technology</span>
    </div>
  </section>
  <p class="format-label" style="top:372px">Website Header</p>

  <section class="banner banner--social">
    <div class="banner__wave" role="img" aria-label="Flowing blue-to-purple dotted wave mesh"></div>
    <span class="banner__word" style="left:39px; top:34px">Engaged</span>
    <span class="banner__word" style="left:183px; top:34px">Connected</span>
    <span class="banner__word" style="left:39px; top:70px">Support</span>
    <span class="banner__word" style="left:183px; top:70px">Ethical Technology</span>
    <div class="brand">
      <span class="brand__dot"></span>
      <span class="brand__name">Kestrelane Technology</span>
    </div>
  </section>
  <p class="format-label" style="top:636px">Brindlepost Header</p>

  <section class="banner banner--email">
    <div class="banner__wave" role="img" aria-label="Flowing blue-to-purple dotted wave mesh"></div>
    <span class="banner__word" style="left:18px; top:37px">Engaged</span>
    <span class="banner__word" style="left:104px; top:37px">Connected</span>
    <span class="banner__word" style="left:18px; top:63px">Support</span>
    <span class="banner__word" style="left:104px; top:63px">Ethical Technology</span>
    <div class="brand">
      <span class="brand__dot"></span>
      <span class="brand__name">Kestrelane Technology</span>
    </div>
  </section>
  <p class="format-label" style="top:876px">Email Marketing</p>

  <section class="banner banner--ad">
    <div class="banner__wave" role="img" aria-label="Flowing blue-to-purple dotted wave mesh"></div>
    <span class="banner__word" style="top:12px">Support</span>
    <span class="banner__word" style="top:28px">Engaged</span>
    <span class="banner__word" style="top:44px">Connected</span>
    <span class="banner__word" style="top:60px">Ethical Technology</span>
    <div class="brand">
      <span class="brand__dot"></span>
      <span class="brand__name">Kestrelane Technology</span>
    </div>
  </section>
  <p class="format-label" style="top:1142px">Advertising</p>

</body>
</html>
```